Real Estate "For Sale" Sign for construction company

We need a sign that we can use to hang on a post and place on the road when we sell a property. The sign will be simple and will need to mainly feature our logo (files attached), as well as the words "For Sale", and then our phone number "(555) 617 3489". The sign will hang on a post that'll look something like the attached picture.

Target Market(s)

Home buyers

Industry/Entity Type

Real Estate

Font styles to use
Serif
Sans Serif

Colors
0054AA
0677BA
7BADD7
CADEEF
E8F1F8
0094D4
00A9DD
6FCCEA
C7EBF8
E9F6FB

Requirements
Must have
• For Sale & our phone number

```html
<!DOCTYPE html>
<html lang="en">
<head>
<meta charset="utf-8">
<title>Bluecrest Properties – For Sale Sign</title>
<link href="https://fonts.googleapis.com/css2?family=Montserrat:wght@500;600;700;800&display=swap" rel="stylesheet">
<style>
  :root {
    --sky: #80CCF2;
    --brand-blue: #2A6FAE;
    --brand-mark: #1E4A8F;
    --navy: #1B1A40;
    --indigo: #2B2C6C;
    --royal: #23418F;
    --white: #FFFFFF;
  }
  * { margin: 0; padding: 0; box-sizing: border-box; }
  html, body { width: 900px; height: 1200px; overflow: hidden; }
  body { font-family: "Montserrat", sans-serif; background: var(--sky); }

  .sign { position: relative; width: 900px; height: 1200px; background: var(--sky); }

  .brand { position: absolute; top: 120px; left: 0; width: 900px; text-align: center; }
  .brand-dot { display: block; width: 130px; height: 130px; margin: 0 auto 22px; border-radius: 50%; background: var(--brand-mark); }
  .brand-name { color: var(--brand-blue); font-weight: 500; font-size: 60px; line-height: 1; letter-spacing: 1px; }
  .brand-sub { display: block; margin-top: 14px; color: var(--brand-blue); font-weight: 500; font-size: 22px; letter-spacing: 24px; padding-left: 24px; }

  .banner { position: absolute; top: 422px; left: 0; width: 900px; height: 355px; background: var(--navy); }
  .banner-title { position: absolute; top: 122px; left: 0; width: 900px; text-align: center; color: var(--white); font-weight: 700; font-size: 134px; line-height: 1; letter-spacing: 3px; }

  .contact { position: absolute; left: 0; width: 900px; text-align: center; }
  .contact-prompt { top: 862px; color: var(--royal); font-weight: 800; font-size: 37px; letter-spacing: 1.5px; line-height: 1; }
  .contact-phone { top: 950px; color: var(--indigo); font-weight: 700; font-size: 92px; letter-spacing: 3px; line-height: 1; word-spacing: 14px; }
  .contact-web { top: 1092px; color: var(--navy); font-weight: 600; font-size: 31px; letter-spacing: 2px; line-height: 1; }
</style>
</head>
<body>
  <main class="sign">
    <header class="brand">
      <span class="brand-dot" aria-hidden="true"></span>
      <div class="brand-name">Bluecrest</div>
      <span class="brand-sub">PROPERTIES</span>
    </header>

    <section class="banner">
      <h1 class="banner-title">FOR SALE</h1>
    </section>

    <p class="contact contact-prompt">CALL OR TEXT ME AT :</p>
    <p class="contact contact-phone">(555) 617 3489</p>
    <p class="contact contact-web">www.bluecrestproperties.com</p>
  </main>
</body>
</html>
```